Business card design for Plumbing and Gas fitting company

We need a business card design for our plumbing and gas fitting company using the company logo and director details. Design should be modern and eye-catching however kept reasonably simple. This design should be targeted at commercial businesses/work so professionalism is key.

Target Market(s)

Commercial/business

Industry/Entity Type

Plumbing

Contact Information for Business Card

Warren Dohey
Director
027 581 9043
warren@vantorplumbingandgas.example
PO Box 7816
Palmerston North 4472

Font styles to use
Sans Serif

Requirements
Must have
• Logo
• Modern
• Kept simple
Nice to have
• Colour scheme based around logo

```html
<!DOCTYPE html>
<html lang="en">
<head>
<meta charset="utf-8">
<title>Vantor Plumbing &amp; Gas – Business Card</title>
<link rel="stylesheet" href="https://fonts.googleapis.com/css2?family=Open+Sans:wght@400;600;700&display=swap">
<style>
  :root {
    --stage: #dfe3e8;
    --card-dark: #434343;
    --card-light: #ffffff;
    --brand-blue: #1a72be;
    --brand-orange: #de7a30;
    --text-grey: #666a6e;
    --muted-grey: #a9a9a9;
  }
  * { box-sizing: border-box; margin: 0; padding: 0; }
  html, body {
    width: 1200px; height: 675px; overflow: hidden;
    background: var(--stage);
    font-family: "Open Sans", sans-serif;
  }
  .canvas {
    position: relative; width: 1200px; height: 675px;
    display: flex; align-items: center; justify-content: center; gap: 40px;
  }
  .card {
    position: relative; width: 520px; height: 297px; overflow: hidden;
    box-shadow: 0 10px 28px rgba(40, 50, 65, 0.22);
  }
  /* Back */
  .card-back {
    background: var(--card-dark);
    display: flex; flex-direction: column; align-items: center; justify-content: center;
  }
  .card-back .brand-name {
    color: var(--brand-blue); font-weight: 700; font-size: 30px; letter-spacing: 0.2px;
  }
  .card-back .website {
    margin-top: 34px; color: var(--muted-grey); font-size: 15px; letter-spacing: 0.8px;
  }
  /* Front */
  .card-front { background: var(--card-light); }
  .name-tab {
    position: absolute; left: 0; top: 96px; width: 14px; height: 40px;
    background: var(--brand-blue); border-radius: 0 5px 5px 0;
  }
  .person { position: absolute; left: 64px; top: 94px; }
  .person .name { color: var(--brand-blue); font-size: 21px; font-weight: 400; line-height: 1.1; }
  .person .role { color: var(--text-grey); font-size: 14px; letter-spacing: 0.6px; margin-top: 3px; }
  .card-front .brand-name {
    position: absolute; right: 28px; top: 40px;
    color: var(--brand-blue); font-weight: 700; font-size: 18px;
  }
  .contact {
    position: absolute; left: 64px; top: 166px; list-style: none;
    color: var(--text-grey); font-size: 13.5px; line-height: 23px;
  }
  .contact li { display: flex; align-items: center; gap: 8px; }
  .contact svg { width: 14px; height: 14px; fill: var(--brand-blue); flex: none; }
  .swoosh { position: absolute; left: 0; bottom: 0; width: 520px; height: 297px; }
  .swoosh .band-blue { fill: var(--brand-blue); }
  .swoosh .band-orange { fill: var(--brand-orange); }
</style>
</head>
<body>
<main class="canvas">
  <section class="card card-back" aria-label="Card back">
    <div class="brand-name">Vantor Plumbing &amp; Gas</div>
    <div class="website">www.vantorplumbingandgas.example</div>
  </section>

  <section class="card card-front" aria-label="Card front">
    <svg class="swoosh" viewBox="0 0 520 297" aria-hidden="true">
      <path class="band-blue" d="M150,297 Q360,246 520,186 L520,222 Q390,268 260,297 Z"/>
      <path class="band-orange" d="M10,297 Q190,258 360,228 Q200,270 90,297 Z"/>
    </svg>
    <div class="name-tab"></div>
    <div class="brand-name">Vantor Plumbing &amp; Gas</div>
    <div class="person">
      <div class="name">Warren Dohey</div>
      <div class="role">DIRECTOR</div>
    </div>
    <ul class="contact">
      <li>
        <svg viewBox="0 0 24 24" aria-hidden="true"><path d="M6.6 10.8a15.1 15.1 0 0 0 6.6 6.6l2.2-2.2a1 1 0 0 1 1-.25 11.4 11.4 0 0 0 3.6.57 1 1 0 0 1 1 1V20a1 1 0 0 1-1 1A17 17 0 0 1 3 4a1 1 0 0 1 1-1h3.5a1 1 0 0 1 1 1c0 1.25.2 2.45.57 3.57a1 1 0 0 1-.25 1z"/></svg>
        027 581 9043
      </li>
      <li>
        <svg viewBox="0 0 24 24" aria-hidden="true"><path d="M2 5h20v14H2z M4 7v.4l8 5.2 8-5.2V7l-8 5.2z" fill-rule="evenodd"/></svg>
        warren@vantorplumbingandgas.example
      </li>
      <li>PO Box 7816, Palmerston North 4472</li>
    </ul>
  </section>
</main>
</body>
</html>
```